The most modern business card ever !!!

Our company call “Vantilo”. Vantilo is a technology company specialized in cruises solutions. Out main product is a platform to reserve cruises. This is a revolutionary platform that make easier to travel agencies and final users to reserve cruises across dozen companies like tarvik, welbi, dpv, hbt, etc..We are a “start up”, with a young team of developers and we want to transmit it.. For it, we want something different, a modern business card that represent cruises and technology.. When someone receive this card, this person should say: wowww this is different… this is modern… this is a cruise related company..
Contact Information for Business Card
Requirements
Must have
- diferent, modern
Should not have
- traditions business card

```html
<!DOCTYPE html>
<html lang="en">
<head>
<meta charset="utf-8">
<title>Vantilo Business Card</title>
<link href="https://fonts.googleapis.com/css2?family=Montserrat:wght@400;600;700&family=Open+Sans:wght@400&display=swap" rel="stylesheet">
<style>
  :root {
    --backdrop-light: #e4d8c6;
    --backdrop-mid: #cdb99c;
    --backdrop-deep: #b49d7e;
    --glass: rgba(255, 255, 255, 0.16);
    --glass-edge: rgba(255, 255, 255, 0.6);
    --ink: #1a1a1a;
    --ink-soft: #3f3b35;
    --teal: #1f8ca6;
  }
  * { margin: 0; padding: 0; box-sizing: border-box; }
  html, body { width: 1200px; height: 1200px; overflow: hidden; }
  body {
    position: relative;
    font-family: "Montserrat", sans-serif;
    background:
      radial-gradient(circle at 78% 30%, rgba(240, 236, 228, 0.7) 0 90px, transparent 220px),
      radial-gradient(circle at 85% 80%, rgba(214, 226, 232, 0.55) 0 60px, transparent 200px),
      radial-gradient(circle at 25% 60%, rgba(150, 126, 98, 0.45) 0 80px, transparent 260px),
      radial-gradient(circle at 60% 75%, rgba(120, 98, 76, 0.35) 0 60px, transparent 240px),
      linear-gradient(165deg, var(--backdrop-light) 0%, var(--backdrop-mid) 55%, var(--backdrop-deep) 100%);
  }
  .card {
    position: absolute;
    left: 60px; top: 334px;
    width: 1088px; height: 592px;
    background: linear-gradient(135deg, rgba(255, 255, 255, 0.26) 0%, var(--glass) 45%, rgba(255, 255, 255, 0.1) 100%);
    border: 1.5px solid var(--glass-edge);
    backdrop-filter: blur(14px) saturate(1.1);
    -webkit-backdrop-filter: blur(14px) saturate(1.1);
    box-shadow: inset 0 0 0 1px rgba(255, 255, 255, 0.15), 0 8px 30px rgba(70, 50, 30, 0.12);
  }
  .holder { position: absolute; left: 90px; top: 149px; }
  .holder-name { white-space: nowrap; line-height: 1; }
  .first { font-weight: 700; font-size: 47px; color: var(--ink); letter-spacing: 0.5px; }
  .last { font-weight: 400; font-size: 31px; color: var(--teal); margin-left: 14px; }
  .holder-role {
    margin-top: 12px; margin-left: 18px;
    font-family: "Open Sans", sans-serif;
    font-size: 15px; color: var(--ink-soft); letter-spacing: 0.1px;
  }
  .contacts { position: absolute; left: 110px; top: 263px; list-style: none; }
  .contacts li {
    display: flex; align-items: center;
    height: 50px;
    font-family: "Open Sans", sans-serif;
    font-size: 24px; color: var(--ink);
  }
  .contacts svg { width: 28px; height: 28px; fill: var(--teal); margin-right: 34px; flex: none; }
  .divider {
    position: absolute; left: 519px; top: 72px;
    width: 2px; height: 456px; background: var(--teal);
  }
  .brand {
    position: absolute; left: 570px; top: 245px;
    font-weight: 600; font-size: 100px; line-height: 1;
    color: var(--ink); letter-spacing: 6px;
  }
</style>
</head>
<body>
  <section class="card">
    <div class="holder">
      <div class="holder-name"><span class="first">MAREN</span><span class="last">SOLDE</span></div>
      <div class="holder-role">BUSINESS DEVELOPMENT MANAGER</div>
    </div>
    <ul class="contacts">
      <li><svg viewBox="0 0 24 24"><path d="M12 2a7 7 0 0 0-7 7c0 5 7 13 7 13s7-8 7-13a7 7 0 0 0-7-7zm0 9.5A2.5 2.5 0 1 1 12 6.5a2.5 2.5 0 0 1 0 5z"/></svg>Address</li>
      <li><svg viewBox="0 0 24 24"><path d="M6.6 10.8a15 15 0 0 0 6.6 6.6l2.2-2.2c.3-.3.7-.4 1-.2 1.1.4 2.3.6 3.6.6.6 0 1 .4 1 1V20c0 .6-.4 1-1 1A17 17 0 0 1 3 4c0-.6.4-1 1-1h3.5c.6 0 1 .4 1 1 0 1.3.2 2.5.6 3.6.1.3 0 .7-.2 1z"/></svg>+00 123456789</li>
      <li><svg viewBox="0 0 24 24"><path d="M2 5h20v14H2z M4 7v.4l8 5.6 8-5.6V7l-8 5.5z" fill-rule="evenodd"/></svg>info@vantilo.com</li>
      <li><svg viewBox="0 0 24 24"><path d="M5 2l14 12h-7l4 8-3 1.5-4-8-4 4z"/></svg>www.vantilo.com</li>
    </ul>
    <div class="divider"></div>
    <div class="brand">Vantilo</div>
  </section>
</body>
</html>
```